Skincare company needing leaflet/flyer for selling products

Hi guys. I am needing a leaflet/flyer design for my new skincare business - Brenna skincare. Our products are all made in Australia from natural ingredients. The leaflet should specify that all products have - organic ingredients, cruelty free, no nasty chemicals or ingredients and a made in Australia logo.
The pictures I have supplied, if they can be made more professional looking for the design without any background that would be great. It should look like other competitors and very appealing. The leaflet can be double sided so it looks more easy to read
The information is provided as follows:
Product, skin types the product is for, ml capacity of bottle, key ingredients and price.
Contact is a whatsapp number and website will be up later so if a leaflet can be made with and without the website.
This leaflet/flyer can be easy to read, not hard on the eyes and easy to understand. Focus on blue shades and other calm colours to make it easy on the eyes and attractive to see. Thank you guys for helping
Updates
Getting professional product photos done that can be updated on the leaflet/flyers once received. More submissions are welcomed
Target Market(s)
People wanting good quality skincare that does not contain harmful chemicals and is organic
Look and feel

```html
<!DOCTYPE html>
<html lang="en">
<head>
<meta charset="utf-8">
<title>Brenna Skincare – Product Flyer</title>
<link rel="stylesheet" href="https://fonts.googleapis.com/css2?family=Mulish:wght@300;400;500;600&family=Cormorant+Garamond:wght@500&display=swap">
<style>
  :root{
    --backdrop:#626d73;
    --ink:#141a2e;
    --navy:#10152b;
    --sky-top:#c3ddf2;
    --sky-mid:#eef3f8;
    --accent-blue:#7b9fc9;
    --pill:#b3c8de;
    --dash:#8fb2d8;
    --purple:#a670b4;
    --cyan:#14a9dc;
    --tan:#cfae95;
    --steel:#82a8cf;
    --olive:#c9c43a;
  }
  *{box-sizing:border-box;margin:0;padding:0}
  html,body{width:1200px;height:1200px;overflow:hidden}
  body{background:var(--backdrop);font-family:"Mulish",sans-serif;color:var(--ink);position:relative}

  .flyer-page{
    position:absolute;top:109px;width:462px;height:981px;
    background:linear-gradient(180deg,var(--sky-top) 0%,var(--sky-mid) 30%,#f3f5f8 55%,var(--sky-mid) 80%,var(--sky-top) 100%);
    box-shadow:0 2px 8px rgba(0,0,0,.25);
  }
  .flyer-page--front{left:131px}
  .flyer-page--back{left:607px}

  .brand{position:absolute;left:0;right:0;top:28px;text-align:center}
  .brand-square{width:75px;height:75px;background:var(--navy);margin:0 auto}
  .brand-name{margin-top:22px;font-family:"Mulish",sans-serif;font-weight:500;font-size:26px;letter-spacing:.2em;color:var(--navy)}

  .badges{position:absolute;top:196px;left:54px;display:flex;gap:18px}
  .badge{width:75px;height:75px;border-radius:50%;border:2px solid var(--navy);display:flex;align-items:center;justify-content:center}
  .badge span{width:38px;height:38px;border-radius:50%;background:var(--navy)}

  .product{position:absolute;left:0;width:462px;height:200px}
  .product-photo{position:absolute;left:40px;top:14px;width:66px;height:130px;border-radius:8px;
    background:linear-gradient(180deg,#e9edf1,#ffffff 50%,#d7dde4)}
  .product-photo--dark{background:linear-gradient(180deg,#2b2f33,#15181b 60%,#5b4a3e)}
  .size-pill{position:absolute;left:40px;top:160px;width:66px;height:24px;border-radius:12px;background:var(--pill);
    color:#fff;font-size:10px;font-weight:500;letter-spacing:.04em;display:flex;align-items:center;justify-content:center}
  .product-title{position:absolute;left:125px;top:0;font-size:19px;font-weight:500;letter-spacing:.02em;color:var(--ink)}
  .skin-types{position:absolute;left:125px;top:25px;font-size:12px;font-weight:400;color:var(--accent-blue)}
  .skin-types b{font-weight:400;color:var(--ink);padding:0 3px}
  .price{position:absolute;left:396px;top:-4px;width:42px;height:42px;border-radius:50%;color:#fff;
    font-size:11px;font-weight:500;display:flex;align-items:center;justify-content:center}
  .price--purple{background:var(--purple)}
  .price--cyan{background:var(--cyan)}
  .price--tan{background:var(--tan)}
  .price--steel{background:var(--steel)}
  .price--olive{background:var(--olive)}

  .ingredients{position:absolute;left:125px;top:55px;width:313px;height:128px;border:1px dashed var(--dash);
    border-radius:5px;padding:10px 7px 0 7px}
  .ingredients-label{position:absolute;top:-6px;right:22px;padding:0 6px;background:#f0f4f8;font-size:8.5px;
    font-weight:500;letter-spacing:.06em;color:var(--ink)}
  .ingredient{margin-bottom:4px}
  .ingredient h3{font-size:9.5px;font-weight:500;letter-spacing:.05em;line-height:1.15}
  .ingredient p{font-size:9.3px;font-weight:400;line-height:1.2}

  .product--tall .product-photo{left:40px;top:0;height:166px}
  .product--tall .size-pill{top:176px}
  .product--tall .ingredients{height:146px}
  .product-photo--jar{top:70px!important;height:70px!important;border-radius:12px}

  .contact{position:absolute;left:0;right:0;top:933px;height:28px;display:flex;align-items:center}
  .contact-line{flex:1;height:2px;background:var(--navy)}
  .contact-number{display:flex;align-items:center;gap:10px;padding:0 14px;font-size:21px;font-weight:500;letter-spacing:.05em;color:var(--navy)}
  .contact-dot{width:26px;height:26px;border-radius:50%;background:var(--navy)}
</style>
</head>
<body>

<section class="flyer-page flyer-page--front">
  <header class="brand">
    <div class="brand-square"></div>
    <div class="brand-name">BRENNA SKINCARE</div>
  </header>

  <div class="badges" aria-label="Product promises">
    <div class="badge"><span></span></div>
    <div class="badge"><span></span></div>
    <div class="badge"><span></span></div>
    <div class="badge"><span></span></div>
  </div>

  <article class="product" style="top:300px">
    <div class="product-photo" role="img" aria-label="Hydrating moisturiser pump bottle"></div>
    <div class="size-pill">60ML</div>
    <h2 class="product-title">HYDRATING MOISTURISER</h2>
    <div class="skin-types">Normal<b>|</b>Dry<b>|</b>Mature Skin Types</div>
    <div class="price price--purple">$18</div>
    <div class="ingredients">
      <span class="ingredients-label">KEY INGREDIENTS</span>
      <div class="ingredient"><h3>ROSEHIP OIL</h3><p>Rich in essential fatty acids which are integral for skin regeneration and boosting collagen formation.</p></div>
      <div class="ingredient"><h3>GREEN TEA LEAF EXTRACT</h3><p>Anti-inflammatory benefits which reduce redness and soothes skin irritation.</p></div>
      <div class="ingredient"><h3>DAVIDSON PLUM EXTRACT</h3><p>Improves the appearance of fine lines and wrinkles and rich in antioxidants.</p></div>
    </div>
  </article>

  <article class="product" style="top:511px">
    <div class="product-photo" role="img" aria-label="Balancing moisturiser pump bottle"></div>
    <div class="size-pill">60ML</div>
    <h2 class="product-title">BALANCING MOISTURISER</h2>
    <div class="skin-types">Oily<b>|</b>Combination<b>|</b>Problematic Skin Types</div>
    <div class="price price--cyan">$18</div>
    <div class="ingredients">
      <span class="ingredients-label">KEY INGREDIENTS</span>
      <div class="ingredient"><h3>GRAPE SEED OIL</h3><p>Acts as an anti-inflammatory and effective in combating acne.</p></div>
      <div class="ingredient"><h3>LICORICE ROOT EXTRACT</h3><p>Provides skin brightening effects and soothes itchy and irritated skin.</p></div>
      <div class="ingredient"><h3>QUANDONG (SANDALWOOD) EXTRACT</h3><p>High in vitamin C, reduces the appearance of ageing such as dark circles and pigmentation.</p></div>
    </div>
  </article>

  <article class="product" style="top:722px">
    <div class="product-photo" role="img" aria-label="Eye cream pump bottle"></div>
    <div class="size-pill">15ML</div>
    <h2 class="product-title">EYE CREAM</h2>
    <div class="skin-types">All Skin Types</div>
    <div class="price price--tan">$19</div>
    <div class="ingredients">
      <span class="ingredients-label">KEY INGREDIENTS</span>
      <div class="ingredient"><h3>CUCUMIS SATIVUS (CUCUMBER) SEED OIL</h3><p>Highly moisturising with Vitamin E, it balances the skin &amp; encourages healthy skin regeneration.</p></div>
      <div class="ingredient"><h3>KAKADU PLUM EXTRACT</h3><p>Rich in Vitamin C &amp; Gallic acid which has anti-inflammatory properties, can help reduce pigmentation and dark spots.</p></div>
      <div class="ingredient"><h3>QUANDONG EXTRACT</h3><p>High in Rutin, an antioxidant that soothes skin and calms redness, it also reduces the signs of ageing.</p></div>
    </div>
  </article>

  <footer class="contact">
    <div class="contact-line"></div>
    <div class="contact-number"><span class="contact-dot"></span>0412345678</div>
    <div class="contact-line"></div>
  </footer>
</section>

<section class="flyer-page flyer-page--back">
  <article class="product product--tall" style="top:29px">
    <div class="product-photo" role="img" aria-label="Facial cleansing gel pump bottle"></div>
    <div class="size-pill">125ML</div>
    <h2 class="product-title">FACIAL CLEANSING GEL</h2>
    <div class="skin-types">Oily<b>|</b>Combination<b>|</b>Problematic Skin Types</div>
    <div class="price price--steel">$20</div>
    <div class="ingredients">
      <span class="ingredients-label">KEY INGREDIENTS</span>
      <div class="ingredient"><h3>VITAMIN E</h3><p>A natural antioxidant that helps to protect the face from exposure to the sun and increases skin elasticity. It also reduces acne, blemishes and soothes the skin.</p></div>
      <div class="ingredient"><h3>ALOE VERA JUICE</h3><p>Hydrates &amp; exfoliates the face, reducing inflammation, acne and dry skin.</p></div>
      <div class="ingredient"><h3>KAKADU PLUM EXTRACT</h3><p>Rich in Vitamin C &amp; Gallic acid which has anti-inflammatory properties, can help reduce pigmentation and dark spots. Also stimulates growth of collagen.</p></div>
    </div>
  </article>

  <article class="product product--tall" style="top:255px">
    <div class="product-photo product-photo--dark" role="img" aria-label="Vitamin C serum dropper bottle" style="top:30px;height:136px"></div>
    <div class="size-pill">30ML</div>
    <h2 class="product-title">VITAMIN C SERUM</h2>
    <div class="skin-types">All Skin types</div>
    <div class="price price--tan">$15</div>
    <div class="ingredients">
      <span class="ingredients-label">KEY INGREDIENTS</span>
      <div class="ingredient"><h3>SODIUM PHYTATE</h3><p>Contains stabilising properties that moisturises the skin, helps reduce pore size and improve the appearance of cellulite</p></div>
      <div class="ingredient"><h3>DAVIDSON PLUM EXTRACT</h3><p>Improves the appearance of fine lines and wrinkles and rich in antioxidants.</p></div>
      <div class="ingredient"><h3>VITAMIN C (SODIUM ASCORBYL PHOSPHATE)</h3><p>Contains anti-inflammatory and anti-ageing properties and helps fight acne and blemishes.</p></div>
    </div>
  </article>

  <article class="product product--tall" style="top:481px">
    <div class="product-photo" role="img" aria-label="Perfecting toning mist spray bottle"></div>
    <div class="size-pill">125ML</div>
    <h2 class="product-title">PERFECTING TONING MIST</h2>
    <div class="skin-types">All Skin types</div>
    <div class="price price--purple">$17.5</div>
    <div class="ingredients">
      <span class="ingredients-label">KEY INGREDIENTS</span>
      <div class="ingredient"><h3>ROSE FLOWER WATER</h3><p>Contains anti-ageing properties, hydrates the skin and soothes skin irritation.</p></div>
      <div class="ingredient"><h3>GREEN TEA LEAF EXTRACT</h3><p>Anti-inflammatory benefits which reduce redness and soothes skin irritation.</p></div>
      <div class="ingredient"><h3>KAKADU PLUM</h3><p>Rich in Vitamin C &amp; Gallic acid which has anti-inflammatory properties, can reduce pigmentation and dark spots. It also stimulates growth of collagen and reduces wrinkles.</p></div>
    </div>
  </article>

  <article class="product product--tall" style="top:707px">
    <div class="product-photo product-photo--jar" role="img" aria-label="Body balm jar" style="left:28px;width:90px"></div>
    <div class="size-pill">250ML</div>
    <h2 class="product-title">BODY BALM</h2>
    <div class="skin-types">All Skin Types</div>
    <div class="price price--olive">$15</div>
    <div class="ingredients">
      <span class="ingredients-label">KEY INGREDIENTS</span>
      <div class="ingredient"><h3>KAKADU PLUM EXTRACT</h3><p>Rich in Vitamin C &amp; Gallic acid which has anti-inflammatory properties, can help reduce pigmentation and dark spots. Also stimulates growth of collagen.</p></div>
      <div class="ingredient"><h3>PANTHENOL (VITAMIN B5)</h3><p>An anti-inflammatory skin barrier repairer that improves the appearance of skin, preventing dryness and keeping the skin balanced</p></div>
      <div class="ingredient"><h3>DESERT LIME EXTRACT</h3><p>High in Vitamin C &amp; antioxidants, it vitalises the skin, keeping it nourished and rejuvenated.</p></div>
    </div>
  </article>

  <footer class="contact">
    <div class="contact-line"></div>
    <div class="contact-number"><span class="contact-dot"></span>0412345678</div>
    <div class="contact-line"></div>
  </footer>
</section>

</body>
</html>
```